Broschüre
Zielgruppe
Wir sind eine ambulanter Pflegedienst in Rostock. Ab dem Herbst 25 bieten wir für Interessenten mit einem Pflegegrad begleitete reisen an. Eine Fachkraft wird Patienten mit Pflegegrad in kleinen Gruppen begleiten. Den Text für den Flyer haben wir eingefügt. Bitte die Bider aus dem Stock Portal wählen. Über den Flyer sollen Patienten gefunden werden.
Der Flyer
sollte Serios wirken und Reiselust der Senioren wecken.
Aufgabenstellung
Hier der Text für den Flyer:
Was wir bieten:
✔️ Begleitung durch erfahrene Pflegefachkräfte ✔️ Körperpflege, Medikamentengabe & Betreuung wie zuhause ✔️ 24-Stunden-Erreichbarkeit unserer Pflegekräfte vor Ort im gebuchten Hotel ✔️ Zusammenarbeit mit ausgewählten Hotels – barrierefrei & seniorengerecht ✔️ Kleine Gruppen & individuelle Betreuung vor Ort
Gut zu wissen:
Für unsere pflegerische Begleitung entstehen Ihnen keine zusätzlichen Kosten, wenn Sie einen Pflegegrad haben und das Verhinderungspflege-Budget noch nicht aufgebraucht ist.
Lediglich die Hotelkosten sind von Ihnen selbst zu tragen.
Wer hat Anspruch auf Verhinderungspflege?
Alle Pflegebedürftigen mit einem anerkannten Pflegegrad ab Stufe 2 können jährlich Verhinderungspflege über die Pflegekasse abrufen – ideal, um sich im Urlaub sicher begleiten zu lassen!
Unser Service – Ihr Mehrwert:
Wir organisieren Ihre Reise von A bis Z und begleiten Sie oder Ihre Angehörigen auf dem Weg zu Erholung und neuen Eindrücken – mit Herz, Kompetenz und Erfahrung. Vor Ort sind müssen Sie auf nichts verzichten und werden versorgt wie zu Hause. Gerne organisieren wir auch die Abholung aus ihrer Hässlichkeit.
???? Sonnenweg Touren – Ihr verlässlicher Partner für Pflege und Lebensfreude
???? Jetzt informieren & Platz sichern: 0381 - 72946183
???? Mail@sonnenweg-touren .de
???? www.sonnenweg-touren.de

```html
<!DOCTYPE html>
<html lang="de">
<head>
<meta charset="utf-8">
<title>Sonnenweg Touren – Flyer</title>
<link href="https://fonts.googleapis.com/css2?family=Poppins:wght@500;600;700&display=swap" rel="stylesheet">
<style>
:root{
  --navy:#1c2a4f;
  --orange:#ea6b2d;
  --lavender:#c6cbe0;
  --paper:#ffffff;
  --stage:#eceef2;
  --logo-blue:#2f6fba;
}
*{box-sizing:border-box;margin:0;padding:0}
html,body{width:1200px;height:1200px;overflow:hidden}
body{background:var(--stage);font-family:"Poppins",sans-serif;position:relative}
.page{position:absolute;top:319px;width:580px;height:562px;background:var(--paper);overflow:hidden;box-shadow:0 4px 14px rgba(0,0,0,.18)}
.page--front{left:13px}
.page--back{left:607px}
.photo{position:absolute;left:0;top:0;width:580px;height:268px}
.photo--couple{background:linear-gradient(180deg,#f4f6f8 0%,#dfe6ea 28%,#a9b59a 50%,#c9ccbf 62%,#7a8a55 100%)}
.photo--coast{background:linear-gradient(180deg,#f5f6f7 0%,#d8dfe2 30%,#9fae8e 55%,#d4d6cf 70%,#6f8450 100%)}
.decor{position:absolute;left:0;top:0;width:580px;height:562px}
.inset{position:absolute;left:440px;top:48px;width:140px;height:132px}
.brand{position:absolute;left:20px;top:22px;display:flex;align-items:center;gap:8px}
.brand__dot{width:28px;height:28px;border-radius:50%;background:var(--logo-blue)}
.brand__name{font-weight:600;font-size:17px;color:var(--navy)}
.content{position:absolute;left:0;width:580px;text-align:center;color:#fff}
.title{font-weight:600;font-size:34px;line-height:1.1}
.subtitle{font-weight:700;font-size:13px;line-height:18px;color:var(--orange);margin-top:2px}
.pill{display:inline-block;background:var(--orange);color:#fff;font-weight:700;border-radius:12px;padding:1px 12px}
.pill--sm{font-size:14px}
.benefits{list-style:none;margin-top:6px;font-size:10.4px;font-weight:600;line-height:17px}
.benefits li::before{content:"✔";color:var(--orange);font-size:12px;margin-right:4px}
.note{font-size:10.4px;font-weight:600;line-height:13.5px;margin-top:20px}
.back-block{font-size:10.4px;font-weight:600;line-height:13.5px;margin-top:5px}
.cta{font-weight:700;font-size:15px}
.contact{font-size:10.4px;font-weight:600;line-height:13.5px}
</style>
</head>
<body>

<section class="page page--front">
  <div class="photo photo--couple" role="img" aria-label="Foto: Seniorenpaar mit Sonnenhüten macht ein Selfie vor einer Flusslandschaft"></div>
  <svg class="decor" viewBox="0 0 580 562" aria-hidden="true">
    <path d="M0 258 H580 V562 H0 Z" fill="var(--navy)"/>
    <path d="M0 218 C45 226 72 258 66 292 C60 324 28 340 0 352 Z" fill="var(--orange)"/>
    <path d="M0 520 C28 526 58 545 78 562 H0 Z" fill="var(--lavender)"/>
    <path d="M580 440 C542 446 518 482 514 562 H580 Z" fill="var(--lavender)"/>
    <path d="M580 330 C540 350 522 392 544 440 C560 478 568 515 580 540" fill="none" stroke="var(--orange)" stroke-width="2"/>
    <path d="M36 562 C58 544 100 544 122 562" fill="none" stroke="var(--orange)" stroke-width="2"/>
    <path d="M415 0 C430 30 470 40 478 80 C484 110 500 125 520 130" fill="none" stroke="var(--orange)" stroke-width="2"/>
  </svg>
  <svg class="inset" viewBox="0 0 140 132" role="img" aria-label="Foto: Seniorin jubelt mit erhobenen Armen in der Natur">
    <defs><linearGradient id="g-inset-a" x1="0" y1="0" x2="0" y2="1"><stop offset="0" stop-color="#c9dceb"/><stop offset=".55" stop-color="#a7b98c"/><stop offset="1" stop-color="#5f7a3d"/></linearGradient></defs>
    <path d="M30 22 C60 -2 118 30 140 64 V122 C100 132 50 128 26 102 C2 76 4 42 30 22 Z" fill="url(#g-inset-a)" stroke="var(--navy)" stroke-width="5"/>
  </svg>
  <div class="brand"><span class="brand__dot"></span><span class="brand__name">Pflegeteam Sonnenweg</span></div>

  <div class="content" style="top:270px">
    <h1 class="title">Sonnenweg Touren –</h1>
    <p class="subtitle">Ihr verlässlicher Partner für Pflege und Lebensfreude</p>
    <div style="margin-top:8px"><span class="pill pill--sm">Was wir bieten:</span></div>
    <ul class="benefits">
      <li>Begleitung durch erfahrene Pflegefachkräfte</li>
      <li>Körperpflege, Medikamentengabe &amp; Betreuung wie zuhause</li>
      <li>24-Stunden-Erreichbarkeit unserer Pflegekräfte vor Ort im gebuchten Hotel</li>
      <li>Zusammenarbeit mit ausgewählten Hotels – barrierefrei &amp; seniorengerecht</li>
      <li>Kleine Gruppen &amp; individuelle Betreuung vor Ort</li>
    </ul>
    <p class="note">Für unsere pflegerische Begleitung entstehen Ihnen<br>keine zusätzlichen Kosten, wenn Sie einen Pflegegrad haben und das<br>Verhinderungspflege-Budget noch nicht aufgebraucht ist.<br>Lediglich die Hotelkosten sind von Ihnen selbst zu tragen.</p>
  </div>
</section>

<section class="page page--back">
  <div class="photo photo--coast" role="img" aria-label="Foto: Seniorenpaar mit Hüten schaut sich lachend an, Flusslandschaft im Hintergrund"></div>
  <svg class="decor" viewBox="0 0 580 562" aria-hidden="true">
    <path d="M0 248 H580 V562 H0 Z" fill="var(--navy)"/>
    <path d="M0 208 C45 216 72 248 66 282 C60 314 28 330 0 342 Z" fill="var(--orange)"/>
    <path d="M0 480 C32 490 66 525 84 562 H0 Z" fill="var(--lavender)"/>
    <path d="M580 340 C548 356 530 388 540 420 C556 468 566 500 580 540" fill="none" stroke="var(--orange)" stroke-width="2"/>
    <path d="M36 562 C62 544 108 544 134 562" fill="none" stroke="var(--orange)" stroke-width="2"/>
    <path d="M415 0 C430 30 470 40 478 80 C484 110 500 125 520 130" fill="none" stroke="var(--orange)" stroke-width="2"/>
  </svg>
  <svg class="inset" viewBox="0 0 140 132" role="img" aria-label="Foto: zwei Seniorinnen genießen den Sonnenuntergang im Garten">
    <defs><linearGradient id="g-inset-b" x1="0" y1="0" x2="0" y2="1"><stop offset="0" stop-color="#f2c47e"/><stop offset=".5" stop-color="#b88a52"/><stop offset="1" stop-color="#5a3a2c"/></linearGradient></defs>
    <path d="M30 22 C60 -2 118 30 140 64 V122 C100 132 50 128 26 102 C2 76 4 42 30 22 Z" fill="url(#g-inset-b)" stroke="var(--navy)" stroke-width="5"/>
  </svg>
  <div class="brand"><span class="brand__dot"></span><span class="brand__name">Pflegeteam Sonnenweg</span></div>

  <div class="content" style="top:262px">
    <span class="pill" style="font-size:14.5px">Wer hat Anspruch auf Verhinderungspflege?</span>
    <p class="back-block">Alle Pflegebedürftigen mit einem anerkannten Pflegegrad ab Stufe 2<br>können jährlich Verhinderungspflege über die Pflegekasse abrufen –<br>ideal, um sich im Urlaub sicher begleiten zu lassen!</p>
    <div style="margin-top:18px"><span class="pill" style="font-size:14.5px">Unser Service – Ihr Mehrwert:</span></div>
    <p class="back-block">Wir organisieren Ihre Reise von A bis Z und begleiten Sie oder Ihre Angehörigen auf<br>dem Weg zu Erholung und neuen Eindrücken – mit Herz, Kompetenz und Erfahrung.<br>Vor Ort sind müssen Sie auf nichts verzichten und werden versorgt wie zu Hause.<br>Gerne organisieren wir auch die Abholung aus ihrer Hässlichkeit.</p>
  </div>
  <div class="content" style="top:470px">
    <p class="cta">Jetzt informieren &amp; Platz sichern: 0381 - 72946183</p>
    <p class="contact" style="margin-top:16px">Mail@sonnenweg-touren .de<br>www.sonnenweg-touren.de</p>
  </div>
</section>

</body>
</html>
```